New Bicycle shop business card

Hi!
I'm looking for a business card for my new proffesional bike mechanics shop. This shop is only for fixing broken bikes and not selling bikes.
Peferbly a modern and sleek and modern design.
Colors: black, grey, red, white
Information:
Name: Rijwielwerkplaats Vanhoutem
Shop owner: Bart Vanhoutem & Sanne Maertens
Website: www.rijwielwerkplaats-vanhoutem.be
Email: info@rijwielwerkplaats-vanhoutem.be
Phone number: +32471902386
Street adres: Kerkweg 64
9970 Oostmoere
Slogan/shop information: Herstellingen van alle merken.
Logo: see files.
Target Market(s)
People who seek a mechanic to fix or upgrade their bikes.
Contact Information for Business Card
Information:
Website: info@rijwielwerkplaats-vanhoutem.be
9970 Oostmoere
Logo: see files.

```html
<!DOCTYPE html>
<html lang="nl">
<head>
<meta charset="utf-8">
<title>Rijwielwerkplaats Vanhoutem – visitekaartje</title>
<link rel="stylesheet" href="https://fonts.googleapis.com/css2?family=Open+Sans:wght@400;600;700;800&display=swap">
<style>
  :root {
    --ink: #0a0a0b;
    --card-black: #0c0c0d;
    --paper: #ffffff;
    --red: #e8213f;
    --grey: #a7a9ac;
    --stage: #e9e9eb;
    --text-light: #f2f2f2;
  }
  * { margin: 0; padding: 0; box-sizing: border-box; }
  html, body { width: 1200px; height: 900px; overflow: hidden; }
  body {
    background: var(--stage);
    font-family: "Open Sans", Arial, sans-serif;
    display: flex; flex-direction: column; align-items: center; justify-content: center;
    gap: 50px;
  }
  .card {
    position: relative;
    width: 660px; height: 380px;
    border-radius: 36px;
    overflow: hidden;
    background: var(--card-black);
    box-shadow: 0 10px 30px rgba(0,0,0,.18);
  }
  .card__shape { position: absolute; inset: 0; }

  /* front */
  .brand {
    position: absolute; left: 30px; top: 78px; width: 240px;
    display: flex; flex-direction: column; align-items: center; gap: 14px;
    text-align: center;
  }
  .brand__dot { width: 44px; height: 44px; border-radius: 50%; background: var(--red); }
  .brand__name {
    color: var(--ink); font-weight: 800; font-size: 18px; line-height: 1.2;
    text-transform: uppercase; letter-spacing: .04em;
  }
  .contact {
    position: absolute; right: 36px; top: 92px; width: 280px;
    text-align: right; color: var(--text-light);
  }
  .contact__label { color: var(--red); font-size: 14px; font-weight: 600; }
  .contact__owners { font-size: 15px; font-weight: 700; margin-top: 2px; white-space: nowrap; }
  .contact__company { color: var(--red); font-size: 16px; font-weight: 700; margin-top: 6px; white-space: nowrap; }
  .contact__role { font-size: 12px; font-weight: 600; margin-bottom: 12px; }
  .contact__line { font-size: 12px; line-height: 1.6; display: flex; justify-content: flex-end; align-items: center; gap: 8px; white-space: nowrap; }
  .contact__icon { width: 14px; height: 14px; flex: none; }

  /* back */
  .card__pattern { position: absolute; inset: 0; }
  .back-brand {
    position: absolute; left: 50%; top: 130px; transform: translateX(-50%);
    display: flex; flex-direction: column; align-items: center; gap: 14px;
  }
  .back-brand__dot { width: 52px; height: 52px; border-radius: 50%; background: var(--red); }
  .back-brand__name { color: var(--text-light); font-size: 16px; font-weight: 700; text-transform: uppercase; letter-spacing: .04em; white-space: nowrap; }
  .slogan {
    position: absolute; left: 44px; bottom: 40px;
    color: var(--text-light); font-size: 16px; font-weight: 600;
  }
</style>
</head>
<body>

  <section class="card card--front" aria-label="Voorkant visitekaartje">
    <svg class="card__shape" viewBox="0 0 660 380" width="660" height="380" aria-hidden="true">
      <path d="M0 0 H330 C325 160 250 340 100 380 H0 Z" fill="var(--paper)"/>
      <path d="M330 0 C325 160 250 340 100 380" fill="none" stroke="var(--red)" stroke-width="4"/>
    </svg>

    <div class="brand">
      <span class="brand__dot"></span>
      <span class="brand__name">Rijwielwerkplaats<br>Vanhoutem</span>
    </div>

    <div class="contact">
      <p class="contact__label">Shop owner:</p>
      <p class="contact__owners">Bart Vanhoutem &amp; Sanne Maertens</p>
      <p class="contact__company">Rijwielwerkplaats Vanhoutem</p>
      <p class="contact__role">General Manager</p>
      <p class="contact__line">Kerkweg 64</p>
      <p class="contact__line">9970 Oostmoere</p>
      <p class="contact__line">+32471902386
        <svg class="contact__icon" viewBox="0 0 14 14" aria-hidden="true"><rect width="14" height="14" rx="3" fill="var(--paper)"/><path d="M4 3.5c0 3.5 3 6.5 6.5 6.5l.5-1.6-1.7-.8-.8.8C7.3 7.8 6.2 6.7 5.6 5.5l.8-.8-.8-1.7z" fill="var(--red)"/></svg>
      </p>
      <p class="contact__line">info@rijwielwerkplaats-vanhoutem.be
        <svg class="contact__icon" viewBox="0 0 14 14" aria-hidden="true"><rect width="14" height="14" rx="3" fill="var(--paper)"/><rect x="3" y="4" width="8" height="6" fill="var(--red)"/><path d="M3 4l4 3.2L11 4" fill="none" stroke="var(--paper)" stroke-width="1"/></svg>
      </p>
      <p class="contact__line">www.rijwielwerkplaats-vanhoutem.be
        <svg class="contact__icon" viewBox="0 0 14 14" aria-hidden="true"><rect width="14" height="14" rx="3" fill="var(--paper)"/><circle cx="7" cy="7" r="4" fill="none" stroke="var(--red)" stroke-width="1.3"/><path d="M3 7h8M7 3v8" stroke="var(--red)" stroke-width="1"/></svg>
      </p>
    </div>
  </section>

  <section class="card card--back" aria-label="Achterkant visitekaartje">
    <svg class="card__pattern" viewBox="0 0 660 380" width="660" height="380" role="img" aria-label="Faint repeating pattern of the shop emblem">
      <defs>
        <linearGradient id="patternTone" x1="0" y1="0" x2="1" y2="1">
          <stop offset="0" stop-color="#0c0c0d"/>
          <stop offset="1" stop-color="#1a1a1c"/>
        </linearGradient>
      </defs>
      <rect width="660" height="380" fill="url(#patternTone)"/>
    </svg>
    <div class="back-brand">
      <span class="back-brand__dot"></span>
      <span class="back-brand__name">Rijwielwerkplaats Vanhoutem</span>
    </div>
    <p class="slogan">Herstellingen van alle merken.</p>
  </section>

</body>
</html>
```